Traditional style Skull and crossbones craftsmans card for making custom works home decor and more

Brovick Forge surrounding a skull and cross bones. Street address is 417 Marlow Rd N Essex ON. Email is BrovickForge@mailnest.net and telephone number will be 555-314-9086. Use the attached image as a guideline would also like Support your local artist on the card. Our names are Dale and Morgan Brovick

Industry/Entity Type

It Support

Contact Information for Business Card

Standard size with a traditional style font

Font styles to use
Decorative
Script

Requirements
Must have
• 417 Marlow Rd. N Essex ON
• 555-314-9086
• Brovickforge@mailnest.net
• Welding
• Dale and Morgan Brovick
• Support your local artist
Nice to have
• Refer to images for ideas

```html
<!DOCTYPE html>
<html lang="en">
<head>
<meta charset="utf-8">
<title>Brovick Forge – Business Card</title>
<link rel="stylesheet" href="https://fonts.googleapis.com/css2?family=Open+Sans:wght@400;600&family=Quicksand:wght@400;500&display=swap">
<style>
  :root {
    --backdrop: #9a9a9a;
    --card-black: #000000;
    --brand-red: #a41c22;
    --band-red: #a3191f;
    --deep-red: #5a0c0f;
    --text-light: #d9d9d9;
    --text-soft: #e6d0d0;
    --bullet-grey: #cfcfcf;
  }
  * { margin: 0; padding: 0; box-sizing: border-box; }
  html, body { width: 1200px; height: 1000px; overflow: hidden; }
  body { background: var(--backdrop); position: relative; font-family: "Open Sans", Arial, sans-serif; }

  .card { position: absolute; width: 612px; height: 363px; background: var(--card-black); overflow: hidden; }
  .card--front { left: 153px; top: 120px; }
  .card--back { left: 459px; top: 516px; }

  .tagline { position: absolute; left: 84px; top: 40px; font-size: 19.5px; font-weight: 400; letter-spacing: 0.5px; color: var(--text-light); white-space: nowrap; }
  .tagline .accent { color: var(--brand-red); }
  .owners { position: absolute; right: 25px; top: 81px; font-size: 19px; color: var(--brand-red); letter-spacing: 0.3px; white-space: nowrap; }

  .contact-list { position: absolute; left: 160px; top: 124px; list-style: none; }
  .contact-item { display: flex; align-items: center; height: 41px; font-family: "Quicksand", Arial, sans-serif; font-size: 18px; color: var(--text-light); white-space: nowrap; }
  .contact-icon { width: 28px; height: 28px; margin-right: 12px; flex: none; }

  .services { position: absolute; top: 261px; left: 74px; display: flex; gap: 54px; list-style: none; }
  .service { font-size: 19.5px; color: var(--text-light); letter-spacing: 0.6px; display: flex; align-items: center; white-space: nowrap; }
  .service::before { content: ""; width: 12px; height: 12px; border-radius: 50%; background: var(--brand-red); margin-right: 15px; }

  .craft-band { position: absolute; left: 0; bottom: 0; width: 100%; height: 56px; background: var(--band-red); }
  .crafts { position: absolute; top: 4px; left: 72px; display: flex; list-style: none; }
  .craft { font-family: "Quicksand", Arial, sans-serif; font-size: 19px; color: var(--text-soft); display: flex; align-items: center; white-space: nowrap; margin-right: 46px; }
  .craft::before { content: ""; width: 12px; height: 12px; border-radius: 50%; background: var(--bullet-grey); margin-right: 17px; }

  .backdrop-shards { position: absolute; left: 0; top: 120px; width: 612px; height: 180px; }
  .brand-name { position: absolute; left: 0; width: 100%; top: 140px; text-align: center; font-size: 52px; font-weight: 600; color: var(--brand-red); letter-spacing: 2px; }
  .slogan { position: absolute; left: 0; width: 100%; top: 306px; text-align: center; font-size: 23px; color: var(--text-light); letter-spacing: 0.3px; }
</style>
</head>
<body>

<section class="card card--front" aria-label="Business card front">
  <p class="tagline">SPECIALIZING IN <span class="accent">“ONE OF KIND”</span> DESIGNS</p>
  <p class="owners">Dale and Morgan Brovick</p>

  <ul class="contact-list">
    <li class="contact-item">
      <svg class="contact-icon" viewBox="0 0 28 28" aria-hidden="true">
        <polygon points="14,1 27,10.5 22,26 6,26 1,10.5" fill="var(--brand-red)"/>
        <path d="M14 7a5 5 0 0 0-5 5c0 4 5 9 5 9s5-5 5-9a5 5 0 0 0-5-5z" fill="#fff"/>
        <circle cx="14" cy="12" r="1.8" fill="var(--brand-red)"/>
      </svg>
      417 Marlow Rd. N Essex ON
    </li>
    <li class="contact-item">
      <svg class="contact-icon" viewBox="0 0 28 28" aria-hidden="true">
        <polygon points="14,1 27,10.5 22,26 6,26 1,10.5" fill="var(--brand-red)"/>
        <path d="M10 8l3 0 1 4-2 1.5c.8 1.8 2 3 3.6 3.6L17 15l4 1v3c-6 .5-11.5-5-11-11z" fill="#fff"/>
      </svg>
      555-314-9086
    </li>
    <li class="contact-item">
      <svg class="contact-icon" viewBox="0 0 28 28" aria-hidden="true">
        <polygon points="14,1 27,10.5 22,26 6,26 1,10.5" fill="var(--brand-red)"/>
        <rect x="8" y="10" width="12" height="8.5" fill="#fff"/>
        <polyline points="8,10 14,15 20,10" fill="none" stroke="var(--brand-red)" stroke-width="1.2"/>
      </svg>
      Brovickforge@mailnest.net
    </li>
  </ul>

  <ul class="services">
    <li class="service">BLCAKSMITHING</li>
    <li class="service">CUSTOM WELDING</li>
  </ul>

  <div class="craft-band">
    <ul class="crafts">
      <li class="craft">Designing</li>
      <li class="craft">Building</li>
      <li class="craft">Sculpting</li>
    </ul>
  </div>
</section>

<section class="card card--back" aria-label="Business card back">
  <svg class="backdrop-shards" viewBox="0 0 612 180" role="img" aria-label="Jagged dark red torn-edge backdrop behind the brand name">
    <rect x="0" y="20" width="612" height="140" fill="var(--deep-red)" opacity="0.75"/>
  </svg>
  <p class="brand-name">Brovick Forge</p>
  <p class="slogan">Support your local artist</p>
</section>

</body>
</html>
```